Redesign Login page

I want to redesign my login page to bring my 2 products closer together. I am only looking to redesign one login page, not 2.

For the logo, please make it solid and it can be black or white if helpful. I can also fine tune the logo if you get it close.

Coding

Coded - Design and coding required

Number of Pages Required

1 page

```html
<!DOCTYPE html>
<html lang="en">
<head>
<meta charset="utf-8">
<title>Northvale – Sign in</title>
<link rel="stylesheet" href="https://fonts.googleapis.com/css2?family=Arimo:wght@400;700&display=swap">
<style>
  :root {
    --bg: #eef1f0;
    --bg-shade: #c9d1cf;
    --card: #ffffff;
    --brand: #42635e;
    --ink: #111111;
    --muted: #6b6b6b;
    --field: #f2f3f3;
    --icon: #b9bcbc;
    --line: #d9dcdc;
    --orbitly: #3b7be0;
    --quadrant: #f0a020;
  }
  * { box-sizing: border-box; margin: 0; padding: 0; }
  html, body { width: 1200px; height: 800px; overflow: hidden; }
  body {
    font-family: "Arimo", Arial, sans-serif;
    color: var(--ink);
    background:
      radial-gradient(circle at 100px 670px, var(--bg-shade) 0, rgba(201,209,207,0) 260px),
      radial-gradient(circle at 1080px 60px, var(--bg-shade) 0, rgba(201,209,207,0) 300px),
      var(--bg);
    position: relative;
  }
  .login-card {
    position: absolute;
    left: 384px; top: 90px;
    width: 433px; height: 610px;
    background: var(--card);
    border-radius: 48px;
    border-top: 6px solid var(--brand);
    box-shadow: 0 10px 30px rgba(0,0,0,0.05);
  }
  .welcome {
    position: absolute; top: 48px; left: 0; right: 0;
    text-align: center; font-size: 18px; letter-spacing: 0.2px;
  }
  .brand-name {
    position: absolute; top: 80px; left: 0; right: 0;
    text-align: center; font-size: 44px; font-weight: 700; letter-spacing: -1px;
    color: var(--ink);
  }
  .field {
    position: absolute; left: 50px; width: 333px; height: 49px;
    background: var(--field); border-radius: 14px;
    display: flex; align-items: center; padding: 0 16px 0 18px;
  }
  .field svg.lead { width: 16px; height: 16px; fill: var(--icon); margin-right: 14px; }
  .field .labels { flex: 1; line-height: 1; }
  .field .label { font-size: 13.5px; display: block; margin-bottom: 3px; }
  .field .hint { font-size: 11px; color: var(--muted); }
  .field-email { top: 163px; }
  .field-password { top: 219px; }
  .toggle { width: 24px; height: 16px; }
  .continue {
    position: absolute; top: 275px; left: 50px; width: 333px; height: 49px;
    background: var(--brand); color: #fff; border-radius: 25px;
    display: flex; align-items: center; justify-content: center;
    font-size: 14px; font-weight: 700;
  }
  .continue svg { position: absolute; right: 22px; width: 14px; height: 10px; }
  .options {
    position: absolute; top: 335px; left: 53px; width: 330px;
    display: flex; justify-content: space-between; align-items: center; font-size: 13.5px;
  }
  .remember { display: flex; align-items: center; gap: 10px; }
  .checkbox { width: 18px; height: 18px; border: 1px solid #bfc3c3; border-radius: 4px; }
  .link { color: var(--brand); text-decoration: underline; text-underline-offset: 3px; }
  .signup {
    position: absolute; top: 377px; left: 0; right: 0; text-align: center; font-size: 14px;
  }
  .divider {
    position: absolute; top: 420px; left: 52px; width: 330px; height: 1px; background: var(--line);
  }
  .divider span {
    position: absolute; left: 50%; top: -16px; transform: translateX(-50%);
    width: 32px; height: 32px; border-radius: 50%; background: #fff;
    border: 1px solid var(--line); font-size: 10px;
    display: flex; align-items: center; justify-content: center;
  }
  .sso {
    position: absolute; left: 50px; width: 333px; height: 50px;
    border: 1px solid #cfd2d2; border-radius: 12px; background: #fff;
    display: flex; align-items: center; justify-content: center; gap: 12px; font-size: 14px;
  }
  .sso-orbitly { top: 448px; }
  .sso-quadrant { top: 504px; }
  .mark-circle { width: 18px; height: 18px; border-radius: 50%; background: var(--orbitly); }
  .mark-square { width: 18px; height: 18px; background: var(--quadrant); }
</style>
</head>
<body>
  <main class="login-card">
    <p class="welcome">WELCOME TO</p>
    <h1 class="brand-name">Northvale</h1>

    <div class="field field-email">
      <svg class="lead" viewBox="0 0 16 16"><path d="M1 3h14v10H1z"/><path d="M1 3l7 6 7-6" fill="none" stroke="#f2f3f3" stroke-width="1.4"/></svg>
      <div class="labels"><span class="label">Email</span><span class="hint">Enter your email</span></div>
    </div>

    <div class="field field-password">
      <svg class="lead" viewBox="0 0 16 16"><path d="M5 7V5a3 3 0 0 1 6 0v2" fill="none" stroke="#b9bcbc" stroke-width="1.6"/><rect x="3" y="7" width="10" height="8" rx="2"/></svg>
      <div class="labels"><span class="label">Password</span><span class="hint">**************</span></div>
      <svg class="toggle" viewBox="0 0 24 16" fill="none" stroke="#b9bcbc" stroke-width="1.8"><path d="M1 8s4-6 11-6 11 6 11 6-4 6-11 6S1 8 1 8z"/><circle cx="12" cy="8" r="3"/><path d="M3 1l18 14"/></svg>
    </div>

    <div class="continue">Continue
      <svg viewBox="0 0 14 10" fill="none" stroke="#fff" stroke-width="1.2"><path d="M0 5h13M9 1l4 4-4 4"/></svg>
    </div>

    <div class="options">
      <label class="remember"><span class="checkbox"></span>Remember me</label>
      <span class="link">Forgot Password?</span>
    </div>

    <p class="signup">Don't have an account? <span class="link">Sign up</span></p>

    <div class="divider"><span>OR</span></div>

    <div class="sso sso-orbitly"><span class="mark-circle"></span>Orbitly SSO</div>
    <div class="sso sso-quadrant"><span class="mark-square"></span>Quadrant SSO</div>
  </main>
</body>
</html>
```